Falcrest security business card

Looking for a business card for my security company

Target Market(s)

Security

Industry/Entity Type

Security

Contact Information for Business Card

Name - Gil Marston. Title - General manager - direct 314 862.4490 website www. falcrestsecurityservices.example email - gil@ falcrestsecurityservices.example

Requirements
Must have
• Logo attached

```html
<!DOCTYPE html>
<html lang="en">
<head>
<meta charset="utf-8">
<title>Falcrest Security Services – Business Card</title>
<link rel="stylesheet" href="https://fonts.googleapis.com/css2?family=Roboto:wght@400;700&display=swap">
<style>
  :root {
    --page-bg: #ffffff;
    --front-bg: #121212;
    --gold: #c9a24a;
    --ink: #111111;
    --body-ink: #1c1c1c;
    --white: #ffffff;
    --rule: #d2d2d2;
    --card-edge: #e4e4e4;
  }
  * { margin: 0; padding: 0; box-sizing: border-box; }
  html, body {
    width: 1200px;
    height: 2400px;
    overflow: hidden;
    background: var(--page-bg);
    font-family: "Roboto", Arial, sans-serif;
  }
  .canvas { position: relative; width: 1200px; height: 2400px; }

  .card { position: absolute; }

  .card-front {
    left: 116px; top: 390px;
    width: 965px; height: 551px;
    background: var(--front-bg);
  }
  .card-front .brand-name {
    position: absolute;
    left: 0; right: 0; top: 222px;
    text-align: center;
    font-weight: 700;
    font-size: 92px;
    line-height: 1;
    letter-spacing: 2px;
    color: var(--gold);
  }
  .card-front .web {
    position: absolute;
    left: 0; width: 1004px; top: 483px;
    text-align: center;
    font-size: 21px;
    color: var(--white);
  }

  .card-back {
    left: 127px; top: 1268px;
    width: 970px; height: 553px;
    background: var(--white);
    border: 1px solid var(--card-edge);
  }
  .card-back .brand-name {
    position: absolute;
    left: 540px; width: 360px; top: 112px;
    text-align: center;
    font-weight: 700;
    font-size: 56px;
    line-height: 1;
    letter-spacing: 1px;
    color: var(--ink);
  }
  .person-name {
    position: absolute;
    left: 75px; top: 236px;
    font-weight: 700;
    font-size: 46px;
    line-height: 1;
    color: var(--ink);
  }
  .person-title {
    position: absolute;
    left: 76px; top: 285px;
    font-size: 32px;
    line-height: 1;
    color: var(--ink);
  }
  .divider {
    position: absolute;
    left: 82px; top: 337px;
    width: 809px; height: 2px;
    background: var(--rule);
  }
  .contact-list {
    position: absolute;
    left: 72px; top: 383px;
    list-style: none;
  }
  .contact-item {
    display: flex;
    align-items: center;
    height: 28px;
    margin-bottom: 15px;
    font-size: 23px;
    color: var(--body-ink);
  }
  .contact-item svg {
    width: 25px; height: 25px;
    margin-right: 11px;
    flex: none;
  }
</style>
</head>
<body>
<main class="canvas">

  <section class="card card-front">
    <div class="brand-name">FALCREST</div>
    <div class="web">www. falcrestsecurityservices</div>
  </section>

  <section class="card card-back">
    <div class="brand-name">FALCREST</div>
    <h1 class="person-name">GIL MARSTON</h1>
    <p class="person-title">General manager</p>
    <div class="divider"></div>
    <ul class="contact-list">
      <li class="contact-item">
        <svg viewBox="0 0 24 24" fill="none" stroke="#1c1c1c" stroke-width="1.4" stroke-linejoin="round" aria-hidden="true">
          <path d="M5 2.5l3.5 0.5 1.5 4.5-2.3 1.8a12 12 0 0 0 6.9 6.9l1.8-2.3 4.5 1.5 0.5 3.5-2.4 2.3C11 21.6 2.4 13 2.7 4.9z"/>
        </svg>
        314 862.4490
      </li>
      <li class="contact-item">
        <svg viewBox="0 0 24 24" fill="none" stroke="#1c1c1c" stroke-width="1.4" stroke-linejoin="round" aria-hidden="true">
          <rect x="1.5" y="5" width="21" height="14"/>
          <path d="M1.5 5l10.5 8 10.5-8"/>
        </svg>
        gil@ falcrestsecurityservices.example
      </li>
      <li class="contact-item">
        <svg viewBox="0 0 24 24" fill="none" stroke="#1c1c1c" stroke-width="1.4" aria-hidden="true">
          <circle cx="12" cy="12" r="10"/>
          <ellipse cx="12" cy="12" rx="4.5" ry="10"/>
          <path d="M2 12h20M3.5 7h17M3.5 17h17"/>
        </svg>
        www. falcrestsecurityservices.example
      </li>
    </ul>
  </section>

</main>
</body>
</html>
```